- Redesign our business card
- Logo remains unchanged
- Current business card attached

Target Market(s)

We are a property management company

Industry/Entity Type

Business

```html
<!DOCTYPE html>
<html lang="en">
<head>
<meta charset="utf-8">
<title>Harlow Property Group – Business Card</title>
<link rel="stylesheet" href="https://fonts.googleapis.com/css2?family=Arimo:wght@400;700&family=Roboto+Condensed:wght@700&display=swap">
<style>
  :root {
    --olive: #7b7a3e;
    --beige: #ddd3ab;
    --slate: #6c6c6c;
    --ink: #55554f;
    --paper: #ffffff;
    --backdrop: #ecebe6;
  }
  * { box-sizing: border-box; margin: 0; padding: 0; }
  html, body { width: 1200px; height: 900px; overflow: hidden; }
  body {
    background: var(--backdrop);
    font-family: "Arimo", Arial, sans-serif;
    position: relative;
  }
  .card {
    position: absolute;
    left: 286px;
    width: 634px;
    height: 364px;
    background: var(--paper);
    overflow: hidden;
    box-shadow: 0 6px 18px rgba(0,0,0,0.18);
  }
  .card-front { top: 56px; }
  .card-back { top: 480px; }

  /* Brand lockup */
  .brand { position: absolute; display: flex; align-items: center; gap: 12px; }
  .brand-square { width: 22px; height: 22px; background: var(--beige); flex: none; }
  .brand-name {
    font-weight: 700;
    color: var(--olive);
    letter-spacing: 0.5px;
    white-space: nowrap;
  }
  .brand-tagline {
    position: absolute;
    color: var(--ink);
    text-transform: uppercase;
    letter-spacing: 0.6px;
  }
  .card-front .brand { left: 34px; top: 108px; }
  .card-front .brand-name { font-size: 19px; }
  .card-front .brand-tagline { left: 34px; top: 136px; font-size: 11px; }

  /* Front: name band */
  .name-band {
    position: absolute; left: 0; right: 0; top: 164px; height: 32px;
    background: var(--olive);
  }
  .holder-name {
    position: absolute; right: 238px; top: 0; line-height: 32px;
    font-family: "Roboto Condensed", "Arial Narrow", sans-serif;
    font-weight: 700; font-size: 19px; color: var(--paper);
    text-transform: uppercase; letter-spacing: 0.3px;
  }
  .holder-role {
    position: absolute; right: 0; top: 0; width: 228px; height: 32px;
    background: var(--beige); color: var(--ink);
    font-size: 14px; line-height: 32px; padding-left: 16px;
  }

  /* Front: contact panel */
  .contact-panel {
    position: absolute; left: 0; right: 0; top: 196px; bottom: 0;
    background: var(--slate); color: #f2f2ee;
  }
  .postal {
    position: absolute; left: 350px; top: 18px;
    font-size: 11px; line-height: 16px; text-transform: uppercase;
  }
  .contact-list {
    position: absolute; left: 350px; top: 62px; list-style: none;
    font-size: 11px; line-height: 16px;
  }
  .contact-list .label { color: var(--beige); display: inline-block; width: 14px; }
  .website {
    position: absolute; left: 34px; top: 114px; font-size: 14px;
  }

  /* Back */
  .top-strip { position: absolute; left: 0; right: 0; top: 0; height: 24px; background: var(--olive); }
  .card-back .brand { left: 158px; top: 146px; gap: 16px; }
  .card-back .brand-square { width: 34px; height: 34px; }
  .card-back .brand-name { font-size: 26px; }
  .card-back .brand-tagline { left: 158px; top: 192px; font-size: 16px; }
  .services-band {
    position: absolute; left: 0; right: 0; bottom: 0; height: 48px;
    background: var(--olive); color: var(--paper);
    font-size: 12px; line-height: 48px; padding-left: 158px;
  }
</style>
</head>
<body>
  <section class="card card-front">
    <div class="brand">
      <span class="brand-square"></span>
      <span class="brand-name">HARLOW PROPERTY GROUP</span>
    </div>
    <p class="brand-tagline">Strata Management Services</p>

    <div class="name-band">
      <h1 class="holder-name">Daniel Harlow</h1>
      <p class="holder-role">Licensed Strata Manager</p>
    </div>

    <div class="contact-panel">
      <p class="postal">PO Box 48, Greenfield Park NSW 2176<br>12/5-19 Marlow Street Eastbrook NSW 2031</p>
      <ul class="contact-list">
        <li><span class="label">P</span>: 02 9000 0360</li>
        <li><span class="label">F</span>: 02 9000 4830</li>
        <li><span class="label">M</span>: 0400 000 451</li>
        <li><span class="label">E</span>: info@harlowproperty.com.au</li>
      </ul>
      <p class="website">www.harlowproperty.com.au</p>
    </div>
  </section>

  <section class="card card-back">
    <div class="top-strip"></div>
    <div class="brand">
      <span class="brand-square"></span>
      <span class="brand-name">HARLOW PROPERTY GROUP</span>
    </div>
    <p class="brand-tagline">Strata Management Services</p>
    <p class="services-band">Strata Management | Community Management | Property Management</p>
  </section>
</body>
</html>
```